Marcus Lindqvist Photography needs a business card designs

I am looking for a business card with a logo clean and simple which I can use that logo on my website or on my pictures. It has to be very classy and very professional. Please look at my website at www.marcuslvqphoto.com for my signature. I'm thinking of something like that for my signature/logo. I'm still working on my website but you get an idea. I'm open to any design but not too busy graphics.

I will be printing the business card from qrivel.com.

Surprise me :)

contact me if you have any questions.

-ML

I'm receiving a lot of black background at the moment. I know my website is all black doesn't mean I want my card to be all black. Please send in with some white background as well. Thanks :)

check out some business cards that I found online. I think they are simple and look really awesome. I don't want a card that is too busy.

http://www.marcuslvqphoto.com/p270092084

Reason: Please extend the date for me. I haven't really receive any good design yet.

Printing

• -a logo that related to my first and last initial of my name "ML"
-double sided
• -I don't want my background to be all black.
-no pictures on the card

```html
<!DOCTYPE html>
<html lang="en">
<head>
<meta charset="utf-8">
<title>Marcus Lindqvist Photography – Business Cards</title>
<link rel="stylesheet" href="https://fonts.googleapis.com/css2?family=Gelasio:ital,wght@0,400;1,400&family=Arimo:wght@400&family=Source+Sans+3:wght@400;600&display=swap">
<style>
  :root {
    --page: #ffffff;
    --card: #ffffff;
    --card-edge: #8a8a8a;
    --card-shadow: #cfcfcf;
    --ink: #111111;
    --label: #2a2a2a;
    --muted: #a3a8ab;
  }
  html, body {
    margin: 0;
    padding: 0;
    width: 1200px;
    height: 940px;
    overflow: hidden;
    background: var(--page);
  }
  .sheet {
    position: relative;
    width: 1200px;
    height: 940px;
  }
  .card {
    position: absolute;
    width: 476px;
    height: 309px;
    background: var(--card);
    border: 1px solid var(--card-edge);
    box-shadow: 7px 7px 0 var(--card-shadow);
    box-sizing: border-box;
    overflow: hidden;
  }
  .card--front-emblem { left: 77px;  top: 71px; }
  .card--back-emblem  { left: 633px; top: 71px; }
  .card--front-large  { left: 77px;  top: 556px; }
  .card--back-large   { left: 633px; top: 556px; }

  .studio-name {
    position: absolute;
    margin: 0;
    font-family: "Gelasio", Georgia, serif;
    font-style: italic;
    font-weight: 400;
    font-size: 27px;
    line-height: 1;
    color: var(--ink);
    white-space: nowrap;
  }
  .studio-trade {
    position: absolute;
    margin: 0;
    font-family: "Arimo", Arial, sans-serif;
    font-size: 17px;
    line-height: 1;
    color: var(--ink);
    white-space: nowrap;
  }

  /* Initials mark: plain text with one plain circle beside it */
  .initials {
    position: absolute;
    display: flex;
    align-items: center;
    gap: 12px;
    font-family: "Gelasio", Georgia, serif;
    font-style: normal;
    font-weight: 400;
    color: var(--ink);
    line-height: 1;
    white-space: nowrap;
  }
  .initials__dot {
    flex: none;
    border-radius: 50%;
    background: var(--ink);
  }

  .card--front-emblem .initials { left: 0; right: 0; top: 62px; justify-content: center; font-size: 96px; }
  .card--front-emblem .initials__dot { width: 22px; height: 22px; }
  .card--front-emblem .studio-name { left: 0; right: 0; top: 232px; text-align: center; }
  .card--front-emblem .studio-trade { left: 0; right: 0; top: 262px; text-align: center; }

  .card--back-emblem .initials { left: 80px; top: 122px; font-size: 68px; }
  .card--back-emblem .initials__dot { width: 16px; height: 16px; }

  .card--front-large .studio-name { left: 21px; top: 26px; }
  .card--front-large .studio-trade { left: 21px; top: 56px; }

  .card--front-large .initials,
  .card--back-large .initials {
    right: 24px;
    bottom: 0;
    font-size: 196px;
    gap: 14px;
  }
  .card--front-large .initials__dot,
  .card--back-large .initials__dot { width: 20px; height: 20px; }

  .contact-list {
    position: absolute;
    margin: 0;
    padding: 0;
    list-style: none;
    font-family: "Source Sans 3", Arial, sans-serif;
    color: var(--muted);
  }
  .contact-list__label {
    font-weight: 600;
    color: var(--label);
    margin-right: 3px;
  }
  .card--back-emblem .contact-list {
    left: 262px;
    top: 113px;
    font-size: 17px;
    line-height: 36px;
  }
  .card--back-large .contact-list {
    left: 31px;
    top: 34px;
    font-size: 15.5px;
    line-height: 23px;
  }
</style>
</head>
<body>
<main class="sheet">

  <section class="card card--front-emblem" aria-label="Front, emblem version">
    <div class="initials"><span class="initials__dot"></span>ML</div>
    <p class="studio-name">Marcus Lindqvist</p>
    <p class="studio-trade">Photography</p>
  </section>

  <section class="card card--back-emblem" aria-label="Back, emblem version">
    <div class="initials"><span class="initials__dot"></span>ML</div>
    <ul class="contact-list">
      <li><span class="contact-list__label">T.</span> Phone Number</li>
      <li><span class="contact-list__label">E.</span> Email Address</li>
      <li><span class="contact-list__label">W.</span> Website</li>
    </ul>
  </section>

  <section class="card card--front-large" aria-label="Front, large initials version">
    <p class="studio-name">Marcus Lindqvist</p>
    <p class="studio-trade">Photography</p>
    <div class="initials"><span class="initials__dot"></span>ML</div>
  </section>

  <section class="card card--back-large" aria-label="Back, large initials version">
    <ul class="contact-list">
      <li><span class="contact-list__label">T.</span> Phone Number</li>
      <li><span class="contact-list__label">E.</span> Email Address</li>
      <li><span class="contact-list__label">W.</span> Website</li>
    </ul>
    <div class="initials"><span class="initials__dot"></span>ML</div>
  </section>

</main>
</body>
</html>
```